A hand soap seller needs a premium label for a new product

We need a premium label for a bottle of soap. We want to write on it:
VANTROSELLA (Name)
Hypoallergenic and antibacterial hand soap
350 ml e / 11.8 fl oz (volume, http://pimaxo.ru/7K3RtWbqmeL519)
Saint Petersburg - Russia / www.vantrosella.ru
We want to see the face of a hippopotamus in the design. Use only black and white and green for accents (the color of grass). Examples of a hippopotamus are shown in the photo. Our soap is hypoallergenic. Ideal for both children and adults. Therefore, the label should appeal to adults and children.
The bottle will be white, and the soap dispenser will be black.
So I'm attaching an example of a soap design that we liked
Label size: height-78 mm, width-102 mm !!!

Target Market(s)

Mothers and children

Industry/Entity Type

Hand soap

Font styles to use
Serif

Colors

Designer to choose only greyscale colors for use in the design.

Requirements
Must have
• The face of a hippopotamus emerging from the grass, Black and white palette with elements of green (grass color)
Nice to have
• The face of a hippopotamus emerging from the grass
Should not have
• Different colors

```html
<!DOCTYPE html>
<html lang="en">
<head>
<meta charset="utf-8">
<title>VANTROSELLA Hand Soap Label</title>
<link href="https://fonts.googleapis.com/css2?family=Montserrat:wght@200;600;700&display=swap" rel="stylesheet">
<style>
  :root {
    --page-bg: #ffffff;
    --label-bg: #ffffff;
    --trim-line: #e0254f;
    --ink: #111111;
    --grass: #8bbd2a;
    --grass-dark: #6fa01c;
    --white: #ffffff;
  }
  * { margin: 0; padding: 0; box-sizing: border-box; }
  html, body {
    width: 1200px;
    height: 1200px;
    overflow: hidden;
    background: var(--page-bg);
    font-family: "Montserrat", Arial, sans-serif;
  }
  .canvas {
    position: relative;
    width: 1200px;
    height: 1200px;
  }
  .label {
    position: absolute;
    left: 50px;
    top: 180px;
    width: 1100px;
    height: 841px;
    background: var(--label-bg);
    border: 3px solid var(--trim-line);
  }
  .brand {
    position: absolute;
    top: 62px;
    left: 0;
    width: 100%;
    text-align: center;
    font-weight: 700;
    font-size: 47px;
    letter-spacing: -1px;
    color: var(--ink);
    line-height: 1;
  }
  .brand-rule {
    position: absolute;
    top: 124px;
    left: 477px;
    width: 145px;
    height: 3px;
    background: var(--grass);
  }
  .mascot {
    position: absolute;
    left: 418px;
    top: 160px;
    width: 264px;
    height: 278px;
  }
  .product-name {
    position: absolute;
    top: 432px;
    left: 0;
    width: 100%;
    text-align: center;
    font-weight: 200;
    font-size: 66px;
    line-height: 64px;
    letter-spacing: 18px;
    color: var(--grass);
  }
  .product-name span { display: block; padding-left: 18px; }
  .claim-band {
    position: absolute;
    left: 291px;
    top: 612px;
    width: 519px;
    height: 66px;
    background: var(--grass);
    color: var(--white);
    font-weight: 700;
    font-size: 25px;
    line-height: 29px;
    text-align: center;
    padding-top: 4px;
  }
  .volume-badge {
    position: absolute;
    left: 648px;
    top: 730px;
    width: 118px;
    height: 94px;
  }
  .volume {
    position: absolute;
    left: 632px;
    top: 748px;
    font-weight: 600;
    font-size: 27px;
    line-height: 32px;
    color: var(--ink);
    letter-spacing: -0.5px;
  }
  .volume .imperial { padding-left: 4px; }
</style>
</head>
<body>
  <main class="canvas">
    <section class="label">
      <h1 class="brand">VANTROSELLA</h1>
      <div class="brand-rule"></div>

      <svg class="mascot" viewBox="0 0 264 278" role="img" aria-label="Illustration of a hippopotamus face emerging from the grass inside a green organic shape">
        <path fill="var(--grass)" d="M176 4 C230 6 262 60 262 118 C262 200 212 276 132 276 C58 276 4 226 2 160 C0 110 30 78 70 74 C104 70 114 50 132 30 C146 14 158 4 176 4 Z"/>
      </svg>

      <div class="product-name"><span>Hand</span><span>Soap</span></div>

      <div class="claim-band">Hypoallergenic<br>And Antibacterial</div>

      <svg class="volume-badge" viewBox="0 0 118 94" aria-hidden="true">
        <path fill="var(--grass)" d="M80 2 C104 0 118 18 116 40 C114 70 88 92 52 92 C30 92 18 82 20 66 C22 46 40 34 52 20 C60 10 68 3 80 2 Z"/>
      </svg>
      <p class="volume">350 ml ℮<br><span class="imperial">11.8 fl oz</span></p>
    </section>
  </main>
</body>
</html>
```